New Business card design to reflect rebrand

I would like a business card design with a good base colour for our new logo and also a placeholder for a profile pic of the card holder. the design needs to be editable to the point that we can easily change the picture of the person and use that design for printlarkly etc. we are looking at a metalic finish business card so will need a good base colour to bring out the finish.

Target Market(s)

prospective customers

Industry/Entity Type

Business

Contact Information for Business Card

I would like one editable design that we can change the name of the card holder and profile picture. The design need to be in a format that be send to printlarkly etc.

Our address is Fenwick Lodge, Mill Lane, Ashcombe Vale, KT14 3WB Tel no. 01632 960418

Requirements
Must have
• place holder for a profile pic for the card holder. in AI or preferably PSD format

```html
<!DOCTYPE html>
<html lang="en">
<head>
<meta charset="utf-8">
<title>Fernbrook Workplace Services – Business Card</title>
<link rel="stylesheet" href="https://fonts.googleapis.com/css2?family=Open+Sans:wght@400;600;700&display=swap">
<style>
  :root {
    --page: #e9e7e4;
    --metal-light: #f2f2f2;
    --metal-mid: #dcdcdc;
    --metal-dark: #c4c4c4;
    --navy: #43597a;
    --orange: #ec6a24;
    --text: #4c5566;
    --rule: #45597a;
    --photo-top: #c9ced6;
    --photo-bottom: #2f3a55;
  }
  * { margin: 0; padding: 0; box-sizing: border-box; }
  html, body { width: 1200px; height: 1000px; overflow: hidden; }
  body {
    background: var(--page);
    font-family: "Open Sans", Arial, sans-serif;
    position: relative;
  }
  .card {
    position: absolute;
    left: 265px;
    width: 665px;
    height: 397px;
    background:
      repeating-linear-gradient(0deg, rgba(255,255,255,0.16) 0 1px, rgba(0,0,0,0.025) 1px 2px),
      linear-gradient(110deg, var(--metal-dark) 0%, var(--metal-light) 35%, var(--metal-mid) 60%, var(--metal-light) 82%, var(--metal-dark) 100%);
    box-shadow: 0 4px 12px rgba(0,0,0,0.25);
    overflow: hidden;
  }
  .card--front { top: 73px; }
  .card--back { top: 533px; }

  .brand-name {
    font-weight: 700;
    color: var(--navy);
    letter-spacing: 1px;
    line-height: 1.1;
    display: flex;
    align-items: center;
  }
  .brand-dot {
    border-radius: 50%;
    background: var(--orange);
    flex: none;
  }
  .brand-sub { display: block; font-size: 0.5em; letter-spacing: 3px; }

  .card--front .brand-name {
    position: absolute; left: 33px; top: 66px; font-size: 38px;
  }
  .card--front .brand-dot { width: 20px; height: 20px; margin-right: 14px; }

  .card--back .brand-name {
    position: absolute; left: 0; right: 0; top: 132px;
    justify-content: center; font-size: 58px;
  }
  .card--back .brand-dot { width: 28px; height: 28px; margin-right: 20px; }

  .portrait {
    position: absolute; left: 493px; top: 78px;
    width: 130px; height: 130px; border-radius: 50%;
    background: linear-gradient(180deg, var(--photo-top) 0%, #8d96a6 55%, var(--photo-bottom) 100%);
  }
  .contact { position: absolute; left: 33px; color: var(--text); font-size: 15px; }
  .contact-mobile { top: 219px; }
  .contact-main { top: 261px; line-height: 21px; }
  .contact-address { top: 313px; line-height: 21px; }
  .contact-line { display: flex; align-items: center; gap: 6px; }
  .contact-line svg { width: 13px; height: 13px; fill: var(--text); }
  .divider {
    position: absolute; left: 33px; top: 245px; width: 601px; height: 2px; background: var(--rule);
  }
  .holder { position: absolute; right: 32px; top: 258px; text-align: right; line-height: 1.2; }
  .holder-name { color: var(--orange); font-weight: 700; font-size: 19px; letter-spacing: 0.3px; }
  .holder-role { color: var(--text); font-size: 15px; }
  .bands { position: absolute; left: 0; bottom: 0; width: 665px; height: 24px; }
</style>
</head>
<body>
  <section class="card card--front">
    <div class="brand-name"><span class="brand-dot"></span><span>FERNBROOK<span class="brand-sub">WORKPLACE SERVICES</span></span></div>
    <div class="portrait" role="img" aria-label="Profile photo of the card holder"></div>

    <div class="contact contact-mobile contact-line">
      <svg viewBox="0 0 16 16"><rect x="4" y="0" width="8" height="16" rx="1.5"/><rect x="5.5" y="2" width="5" height="8" fill="#ddd"/></svg>
      + 000 000 000
    </div>
    <div class="divider"></div>
    <div class="contact contact-main">
      <div class="contact-line"><svg viewBox="0 0 16 16"><path d="M1 6c0-2 3-4 7-4s7 2 7 4v1h-4V5H5v2H1zM3 8h10l1 6H2z"/></svg>01632 960733</div>
      <div class="contact-line"><svg viewBox="0 0 16 16"><rect x="0" y="3" width="16" height="10"/><path d="M0 3l8 6 8-6" stroke="#ddd" stroke-width="1.2" fill="none"/></svg>tharlow@fernbrook.com</div>
    </div>
    <div class="contact contact-address">
      Fenwick Lodge, Mill Lane,<br>Ashcombe Vale, KT14 3WB
    </div>

    <div class="holder">
      <div class="holder-name">TOM HARLOW</div>
      <div class="holder-role">Managing Director</div>
    </div>

    <svg class="bands" viewBox="0 0 665 24" preserveAspectRatio="none">
      <polygon points="0,0 340,0 318,24 0,24" fill="var(--orange)"/>
      <polygon points="350,0 665,0 665,24 328,24" fill="var(--navy)"/>
    </svg>
  </section>

  <section class="card card--back">
    <div class="brand-name"><span class="brand-dot"></span><span>FERNBROOK<span class="brand-sub">WORKPLACE SERVICES</span></span></div>
  </section>
</body>
</html>
```